Business Card Design

Want something very unique. No business, just personal. The image I submitted is for inspiration only.

Target Market(s)

friends and new acquaintances

Industry/Entity Type

Business

Contact Information for Business Card

Mara Deltow
Santa Fe, NM
505-271-4906
maradeltow@quillbox.net

```html
<!DOCTYPE html>
<html lang="en">
<head>
<meta charset="utf-8">
<title>Mara Deltow – Personal Card</title>
<link rel="stylesheet" href="https://fonts.googleapis.com/css2?family=Tinos:wght@400&display=swap">
<style>
  :root {
    --backdrop: #e9e6df;
    --frame: #252323;
    --panel: #ebebd7;
    --accent: #e8a81c;
    --ink: #1f1f1f;
    --label-ink: #ffffff;
    --photo-sky: #c9c6b3;
    --photo-rock: #9a6a48;
    --photo-ground: #8a6a3c;
    --photo-shade: #5c5a2e;
  }
  * { box-sizing: border-box; margin: 0; padding: 0; }
  html, body {
    width: 1200px;
    height: 504px;
    overflow: hidden;
    background: var(--backdrop);
    font-family: "Tinos", "Times New Roman", serif;
  }
  .stage {
    position: relative;
    width: 1200px;
    height: 504px;
  }
  .card {
    position: absolute;
    top: 97px;
    width: 540px;
    height: 310px;
    box-shadow: 0 6px 16px rgba(0,0,0,0.25);
  }
  .card-front {
    left: 40px;
    background: var(--frame);
    padding: 38px 34px 42px 34px;
  }
  .panel {
    position: relative;
    width: 100%;
    height: 100%;
    background: var(--panel);
    text-align: center;
    color: var(--ink);
  }
  .name-label {
    position: absolute;
    top: 38px;
    left: 50%;
    transform: translateX(-50%);
    background: var(--accent);
    color: var(--label-ink);
    font-size: 29px;
    letter-spacing: 0.5px;
    padding: 2px 16px 3px;
    white-space: nowrap;
  }
  .contact-list {
    position: absolute;
    top: 108px;
    left: 0;
    right: 0;
    list-style: none;
    font-size: 17px;
    line-height: 26px;
  }
  .contact-list li {
    display: flex;
    align-items: center;
    justify-content: center;
    gap: 4px;
  }
  .contact-list svg {
    width: 15px;
    height: 15px;
    fill: var(--ink);
  }
  .divider {
    position: absolute;
    top: 190px;
    left: 14px;
    right: 14px;
    border-top: 2px dashed var(--accent);
  }
  .social {
    position: absolute;
    top: 203px;
    left: 0;
    right: 0;
    font-size: 15px;
    display: flex;
    justify-content: center;
    align-items: center;
    gap: 10px;
  }
  .social-name {
    font-size: 15px;
    color: var(--ink);
  }
  .card-back {
    left: 620px;
    background: linear-gradient(170deg, var(--photo-sky) 0%, var(--photo-rock) 35%, var(--photo-ground) 65%, var(--photo-shade) 100%);
  }
</style>
</head>
<body>
<main class="stage">
  <section class="card card-front">
    <div class="panel">
      <h1 class="name-label" style="font-weight:400">MARA DELTOW</h1>
      <ul class="contact-list">
        <li>
          <svg viewBox="0 0 16 16" aria-hidden="true"><path d="M8 0.5a5 5 0 0 0-5 5c0 3.8 5 10 5 10s5-6.2 5-10a5 5 0 0 0-5-5zm0 7.2a2.2 2.2 0 1 1 0-4.4 2.2 2.2 0 0 1 0 4.4z"/></svg>
          Santa Fe, NM
        </li>
        <li>
          <svg viewBox="0 0 16 16" aria-hidden="true"><path d="M3.6 1.2l2.2 2.9-1.3 1.6c.9 2 2.4 3.6 4.4 4.6l1.5-1.3 2.9 2.1-1.3 2.6C7 13.2 2.6 8.8 1 3.2z"/></svg>
          505-271-4906
        </li>
        <li>
          <svg viewBox="0 0 16 16" aria-hidden="true"><path d="M1 4h14v9H1z M1.8 4.8l6.2 4.6 6.2-4.6" stroke="var(--panel)" stroke-width="1.2"/></svg>
          maradeltow@quillbox.net
        </li>
      </ul>
      <div class="divider"></div>
      <p class="social">
        Follow Us On
        <span class="social-name">Plaza</span>
        <span class="social-name">Murmel</span>
        <span class="social-name">Kinnect</span>
      </p>
    </div>
  </section>
  <section class="card card-back" role="img" aria-label="Photograph of two people crouching beside resting cheetahs in a sunny rocky enclosure"></section>
</main>
</body>
</html>
```